Veltana corporate website

Dear graphic designers,
We would like to create a brand new corporate website for our company named "Veltana".
Veltana is a small Swiss premium IT company, with very prestigious clients in the Private Banking industry.
Here would be the values which could be associated to Veltana: trustworthy, serious, modern, high tech, high quality, sobriety, elegant.
Please find attached the Veltana logo in SVG format.
Our new website will have for only purpose to present briefly the company in one page: the team of experts (4 employees), the mission, the expertise and the contact info.
Very short and concise, easy to read.
Like this website for example but even shorter: https://www.dorimel-example.com/

```html
<!DOCTYPE html>
<html lang="en">
<head>
<meta charset="utf-8">
<title>Veltana — Swiss premium IT company</title>
<link href="https://fonts.googleapis.com/css2?family=Arimo:wght@400;700&family=Lato:wght@400;700&display=swap" rel="stylesheet">
<style>
:root{
  --blue:#0d4fa3;
  --blue-mid:#0b72bb;
  --blue-light:#7aa9dc;
  --blue-pale:#eef5fc;
  --ink:#1e1e1e;
  --text:#333;
  --white:#fff;
  --dark:#262626;
}
*{box-sizing:border-box;margin:0;padding:0}
html,body{width:1200px;height:2908px;overflow:hidden}
body{position:relative;background:var(--white);font-family:'Lato',sans-serif;color:var(--text)}
.abs{position:absolute}
.heading{font-family:'Arimo',sans-serif;font-weight:700;color:var(--blue);font-size:40px;letter-spacing:.5px}
.heading span{color:var(--blue-light)}
.btn{position:absolute;display:flex;align-items:center;justify-content:center;color:var(--white);font-weight:700;font-size:15px;background:var(--blue);overflow:hidden}
.btn::after{content:"";position:absolute;left:0;right:0;bottom:0;height:10px;background:linear-gradient(176deg,transparent 45%,var(--blue-light) 50%)}
.btn b{position:relative;z-index:1;margin-top:-3px}

/* header */
.site-header{position:absolute;left:0;top:0;width:1200px;height:84px;background:var(--white);z-index:2}
.brand{position:absolute;left:111px;top:22px;font-family:'Lato',sans-serif;font-weight:700;font-size:32px;color:var(--blue);letter-spacing:2px;display:flex;align-items:center;gap:8px}
.brand i{display:block;width:14px;height:14px;border-radius:50%;background:var(--blue)}
.nav a{position:absolute;top:30px;font-size:16px;color:#444;text-decoration:none}
.nav a.active{color:var(--blue);font-weight:700}

/* hero */
.hero{position:absolute;left:0;top:84px;width:1200px;height:476px;overflow:hidden}
.hero-photo{position:absolute;inset:0;background:linear-gradient(90deg,#7e8b98 0%,#a3adb6 35%,#c9cdd2 55%,#6e7784 75%,#5a6f92 100%)}
.hero-title{position:absolute;left:111px;top:130px;font-family:'Arimo',sans-serif;font-weight:700;font-size:60px;color:var(--white)}
.hero-sub{position:absolute;left:111px;top:214px;font-size:34px;color:var(--white)}
.hero-curve{position:absolute;left:0;top:400px;width:1200px;height:160px}

/* mission */
.mission-title{left:111px;top:618px}
.mission-photo{left:111px;top:702px;width:425px;height:277px;background:linear-gradient(135deg,#cfd3d6,#8e8a84 45%,#4c4a4b 80%,#b7b3ac)}
.mission-copy{left:582px;top:619px;width:510px;font-size:15.5px;line-height:28.3px;color:var(--ink)}
.mission-copy p+p{margin-top:18px}

/* expertise */
.expertise{position:absolute;left:0;top:1036px;width:1200px;height:549px;background:linear-gradient(180deg,#0b78bf,#0b52a5)}
.expertise h2{position:absolute;left:0;width:1200px;top:52px;text-align:center;color:var(--white);font-family:'Arimo',sans-serif;font-size:41px}
.card{position:absolute;top:153px;width:268px;height:308px;border:1.5px solid rgba(255,255,255,.8);border-radius:14px;text-align:center;color:var(--white)}
.card .icon{width:125px;height:125px;margin:22px auto 0;background:var(--white);border-radius:50%;display:flex;align-items:center;justify-content:center}
.card h3{margin-top:30px;font-family:'Arimo',sans-serif;font-size:16px;font-weight:700}
.card p{margin-top:8px;font-size:13.5px;line-height:26px}
.arrow{position:absolute;top:290px}

/* team */
.team-title{left:0;width:1200px;text-align:center;top:1640px}
.member{position:absolute;top:1728px;width:260px;text-align:center}
.avatar{width:190px;height:190px;margin:0 auto;border-radius:50%;background:linear-gradient(180deg,#d9d6d2,#8f8a85 60%,#2e3340);box-shadow:5px 5px 0 var(--blue-light)}
.member h4{margin-top:17px;font-family:'Arimo',sans-serif;font-size:19px;color:var(--ink)}
.member .role{font-size:15.5px;color:var(--ink);margin-top:2px}
.member .mail{font-size:15px;color:var(--blue-mid);margin-top:4px}
.member .social{width:16px;height:16px;border-radius:50%;background:var(--blue);margin:18px auto 0}

/* contact */
.contact{position:absolute;left:0;top:2120px;width:1200px;height:788px;background:var(--blue-pale)}
.contact-title{left:0;width:1200px;text-align:center;top:62px}
.lead{left:112px;top:155px;font-size:19px;color:var(--ink)}
.field{position:absolute;background:var(--white);font-size:15px;color:#555;padding:16px 19px;box-shadow:0 2px 4px rgba(0,0,0,.05)}
.divider{left:765px;top:160px;width:1px;height:282px;background:#cfd9e4}
.info-title{font-family:'Arimo',sans-serif;font-weight:700;font-size:23px;color:var(--blue)}
.info-text{font-size:17.5px;color:var(--ink);line-height:33px}

/* footer */
.footer-curve{position:absolute;left:0;top:2650px;width:1200px;height:258px}
.footer-brand{position:absolute;left:0;width:1200px;top:2738px;text-align:center;font-weight:700;font-size:60px;color:var(--blue);letter-spacing:4px}
.footer-nav{position:absolute;left:0;width:1200px;top:2821px;display:flex;justify-content:center;gap:30px;font-size:16px;color:var(--white)}
.copyright{position:absolute;left:0;width:1200px;top:2866px;text-align:center;font-size:16px;color:var(--white)}
</style>
</head>
<body>

<header class="site-header">
  <div class="brand"><i></i>VELTANA</div>
  <nav class="nav">
    <a class="active" style="left:566px">Home</a>
    <a style="left:637px">About</a>
    <a style="left:709px">Team</a>
    <a style="left:775px">Services</a>
    <a style="left:861px">Contact</a>
  </nav>
  <div class="btn" style="left:957px;top:17px;width:132px;height:44px"><b>GET QUOTE</b></div>
</header>

<section class="hero">
  <div class="hero-photo" role="img" aria-label="Two businessmen in suits reviewing a tablet together in an office"></div>
  <h1 class="hero-title">VELTANA</h1>
  <p class="hero-sub">Swiss premium IT company</p>
</section>
<svg class="hero-curve" viewBox="0 0 1200 160" aria-hidden="true">
  <defs><linearGradient id="band" x1="0" x2="1"><stop offset="0" stop-color="#3c86cf"/><stop offset=".5" stop-color="#8ab4e0"/><stop offset="1" stop-color="#1c62b8"/></linearGradient></defs>
  <path d="M0,69 Q560,175 1200,62 L1200,160 L0,160 Z" fill="#fff"/>
  <path d="M0,69 Q560,175 1200,62 L1200,100 Q620,190 0,73 Z" fill="url(#band)"/>
</svg>

<h2 class="abs heading mission-title">OUR <span>MISSION</span></h2>
<div class="abs mission-photo" role="img" aria-label="Three colleagues discussing documents around a laptop in a bright office"></div>
<div class="abs mission-copy">
  <p>Lorem ipsum dolor sit amet, consectetur adipiscing elit, sed do eiusd tempor incididunt ut labore et dolore magna aliqua. Quis ipsum suspendisse ultrices gravida. Risus commodo viverra maecenas accumsan lacus veacilisis.</p>
  <p>Sed ut perspiciatis unde omnis iste natus error sit voluptatem accusantium doloremque laudantium, totam rem aperiam, eaque ipsa quae ab illo inven tore veritatis et quasi architecto beatae vitae dicta sunt plicabo. Nemo enim ipsam voluptatem quia voluptas sit aspernatur augit, sed quia consequuntur magni dolores eos qui ratione voluptatem sequi nesciunt.</p>
</div>
<div class="btn" style="left:582px;top:894px;width:133px;height:44px"><b>LEARN MORE</b></div>

<section class="expertise">
  <h2>EXPERTISE</h2>
  <svg class="arrow" style="left:37px" width="34" height="34" viewBox="0 0 34 34" aria-hidden="true"><circle cx="17" cy="17" r="15.5" fill="none" stroke="rgba(255,255,255,.6)" stroke-width="2"/><path d="M24 17H10M15 11l-6 6 6 6" fill="none" stroke="rgba(255,255,255,.6)" stroke-width="2"/></svg>
  <svg class="arrow" style="left:1127px" width="34" height="34" viewBox="0 0 34 34" aria-hidden="true"><circle cx="17" cy="17" r="15.5" fill="none" stroke="#fff" stroke-width="2"/><path d="M10 17h14M19 11l6 6-6 6" fill="none" stroke="#fff" stroke-width="2"/></svg>

  <div class="card" style="left:146px">
    <div class="icon"><svg width="72" height="72" viewBox="0 0 72 72" fill="none" stroke="#0b6fb8" stroke-width="2.5"><circle cx="27" cy="44" r="19"/><circle cx="45" cy="27" r="19"/><text x="45" y="35" font-size="22" fill="#0b6fb8" stroke="none" text-anchor="middle" font-family="Arimo,sans-serif">$</text><text x="27" y="52" font-size="22" fill="#0b6fb8" stroke="none" text-anchor="middle" font-family="Arimo,sans-serif">€</text></svg></div>
    <h3>CRYPTOCURRENCIES</h3>
    <p>Duis aute irure dolor in reprehender<br>it in voluptate velit esse cillum dolore<br>eu fugiat nulla pariatur.</p>
  </div>
  <div class="card" style="left:466px">
    <div class="icon"><svg width="60" height="72" viewBox="0 0 60 72" fill="none" stroke="#0b6fb8" stroke-width="2.5" stroke-linejoin="round"><rect x="25" y="6" width="10" height="26" rx="5"/><path d="M18 32h24l4 12H14z"/><path d="M14 44l-4 22h40l-4-22M22 56v10M30 56v10M38 56v10"/></svg></div>
    <h3>DATA WIPING</h3>
    <p>Duis aute irure dolor in reprehender<br>it in voluptate velit esse cillum dolore<br>eu fugiat nulla pariatur.</p>
  </div>
  <div class="card" style="left:787px">
    <div class="icon"><svg width="76" height="76" viewBox="0 0 76 76" fill="none" stroke="#0b6fb8" stroke-width="2.5"><circle cx="38" cy="38" r="34"/><circle cx="38" cy="38" r="26"/><circle cx="30" cy="30" r="5"/><circle cx="46" cy="46" r="5"/><path d="M49 25L27 51"/></svg></div>
    <h3>NEGATIVE INTEREST</h3>
    <p>Duis aute irure dolor in reprehender<br>it in voluptate velit esse cillum dolore<br>eu fugiat nulla pariatur.</p>
  </div>
</section>

<h2 class="abs heading team-title">OUR <span>TEAM</span></h2>
<div class="member" style="left:74px"><div class="avatar" role="img" aria-label="Portrait of team member in a dark blazer"></div><h4>Lorin Basset</h4><p class="role">Lorem ipsum dolor sit amet</p><p class="mail">lorin.basset@veltana-mail.com</p><div class="social"></div></div>
<div class="member" style="left:339px"><div class="avatar" role="img" aria-label="Portrait of team member in a light blue shirt"></div><h4>Lorin Basset</h4><p class="role">Lorem ipsum dolor sit amet</p><p class="mail">lorin.basset@veltana-mail.com</p><div class="social"></div></div>
<div class="member" style="left:605px"><div class="avatar" role="img" aria-label="Portrait of team member in a suit and tie"></div><h4>Lorin Basset</h4><p class="role">Lorem ipsum dolor sit amet</p><p class="mail">lorin.basset@veltana-mail.com</p><div class="social"></div></div>
<div class="member" style="left:869px"><div class="avatar" role="img" aria-label="Portrait of team member in a navy suit"></div><h4>Lorin Basset</h4><p class="role">Lorem ipsum dolor sit amet</p><p class="mail">lorin.basset@veltana-mail.com</p><div class="social"></div></div>

<section class="contact">
  <h2 class="abs heading contact-title">CONTACT <span>US</span></h2>
  <p class="abs lead">We’re happy to answer your questions</p>
  <div class="field" style="left:111px;top:199px;width:265px;height:49px">Name:</div>
  <div class="field" style="left:392px;top:199px;width:265px;height:49px">Email:</div>
  <div class="field" style="left:111px;top:266px;width:265px;height:49px">Phone:</div>
  <div class="field" style="left:392px;top:266px;width:265px;height:49px">Subject:</div>
  <div class="field" style="left:111px;top:336px;width:547px;height:96px">Message:</div>
  <div class="btn" style="left:111px;top:458px;width:132px;height:44px"><b>SUBMIT</b></div>
  <div class="abs divider"></div>

  <svg class="abs" style="left:835px;top:165px" width="46" height="52" viewBox="0 0 46 52" fill="none" stroke="#0d4fa3" stroke-width="2.5"><path d="M23 44C12 30 8 23 8 17a15 15 0 0 1 30 0c0 6-4 13-15 27z"/><circle cx="23" cy="17" r="6"/><path d="M12 40c-6 2-8 4-8 6 0 3 9 5 19 5s19-2 19-5c0-2-2-4-8-6"/></svg>
  <h3 class="abs info-title" style="left:905px;top:180px">ADDRESS</h3>
  <p class="abs info-text" style="left:841px;top:231px">Veltana,Addres Comes Here</p>

  <svg class="abs" style="left:835px;top:290px" width="50" height="46" viewBox="0 0 50 46" fill="none" stroke="#0d4fa3" stroke-width="2.5" stroke-linejoin="round"><rect x="14" y="10" width="33" height="24" rx="2"/><path d="M14 12l16 12 17-12"/><path d="M6 4c-4 4-4 12 2 22s14 16 20 16c3 0 5-2 6-4l-6-6-4 3c-4-2-9-8-10-12l3-4-6-7z"/></svg>
  <h3 class="abs info-title" style="left:905px;top:302px">CONNECT</h3>
  <p class="abs info-text" style="left:841px;top:353px">+41 22 555 0190<br>hello@veltana-mail.com</p>
</section>

<svg class="footer-curve" viewBox="0 0 1200 258" aria-hidden="true">
  <defs><linearGradient id="fband" x1="0" x2="1"><stop offset="0" stop-color="#1a5fb6"/><stop offset=".5" stop-color="#8ab4e0"/><stop offset="1" stop-color="#1a5fb6"/></linearGradient></defs>
  <path d="M0,90 Q600,-35 1200,85 L1200,258 L0,258 Z" fill="url(#fband)"/>
  <path d="M0,102 Q620,-10 1200,96 L1200,258 L0,258 Z" fill="#262626"/>
</svg>
<div class="footer-brand">VELTANA</div>
<nav class="footer-nav"><span>Home</span><span>About</span><span>Team</span><span>Services</span><span>Contact</span></nav>
<p class="copyright">© 2023 Veltana. All Rights Reserved.</p>

</body>
</html>
```